Every Drawer Neatly Sorted or EDN Organized needs a business card design. EDN Organized is a professi

We need a business card design that is clean, sharp and conveys a sense of organization. I already have a logo.

Target Market(s)

Families (specifically mothers), small business owners, parents, seniors

Industry/Entity Type

Business

Contact Information for Business Card

My website is www.ednorganized-example.com and my Facebook page is http://www.socialpage-example.com/everydrawerneatlysorted. The phone number is 555-418-2706 and I want to be listed as Miriel O. Dunsford, Owner

Requirements
Must have
• My logo.

```html
<!DOCTYPE html>
<html lang="en">
<head>
<meta charset="utf-8">
<title>EDN Organized — Business Card</title>
<link rel="stylesheet" href="https://fonts.googleapis.com/css2?family=Lato:wght@300;400;700&family=Arimo:wght@400&display=swap">
<style>
  :root {
    --backdrop: #2a2a2a;
    --card-white: #f4f5f6;
    --brand-blue: #2b86d6;
    --brand-blue-deep: #1f6fbd;
    --ink: #1c1c1c;
    --paper: #ffffff;
  }
  * { margin: 0; padding: 0; box-sizing: border-box; }
  html, body {
    width: 1200px;
    height: 997px;
    overflow: hidden;
    background: var(--backdrop);
  }
  .card {
    position: absolute;
    left: 180px;
    top: 258px;
    width: 840px;
    height: 480px;
    border-radius: 26px;
    overflow: hidden;
    background: var(--card-white);
  }
  .card__panel {
    position: absolute;
    inset: 0;
  }
  .card__clip {
    position: absolute;
    left: 92px;
    top: 18px;
    width: 30px;
    height: 78px;
    border-radius: 15px;
    background: var(--brand-blue-deep);
  }
  .holder {
    position: absolute;
    left: 60px;
    top: 150px;
    font-family: "Arimo", Arial, sans-serif;
  }
  .holder__name {
    font-size: 32px;
    color: var(--ink);
    letter-spacing: 0.3px;
  }
  .holder__role {
    margin: 8px 0 0 110px;
    font-size: 22px;
    color: var(--paper);
  }
  .contacts {
    position: absolute;
    left: 40px;
    top: 318px;
    list-style: none;
    font-family: "Lato", Arial, sans-serif;
    font-size: 19px;
    color: var(--ink);
  }
  .contacts__item {
    display: flex;
    align-items: center;
    height: 40px;
  }
  .contacts__icon {
    width: 20px;
    height: 20px;
    margin-right: 26px;
    flex: none;
  }
  .contacts__dot {
    width: 14px;
    height: 14px;
    margin: 0 29px 0 3px;
    border-radius: 50%;
    background: var(--paper);
    opacity: 0.85;
    flex: none;
  }
  .brand {
    position: absolute;
    left: 520px;
    top: 140px;
    width: 290px;
    text-align: center;
    font-family: "Lato", Arial, sans-serif;
    font-weight: 300;
    color: var(--brand-blue-deep);
    font-size: 30px;
    line-height: 1.25;
    letter-spacing: 3px;
    text-transform: uppercase;
  }
</style>
</head>
<body>
  <article class="card" aria-label="EDN Organized business card">
    <svg class="card__panel" width="840" height="480" viewBox="0 0 840 480" aria-hidden="true">
      <defs>
        <linearGradient id="panelBlue" x1="0" y1="0" x2="0" y2="1">
          <stop offset="0" stop-color="#3590de"/>
          <stop offset="1" stop-color="#2478c8"/>
        </linearGradient>
      </defs>
      <polygon points="0,62 330,62 600,480 0,480" fill="url(#panelBlue)"/>
    </svg>

    <div class="card__clip" role="img" aria-label="Paperclip illustration"></div>

    <div class="holder">
      <p class="holder__name">Miriel O. Dunsford</p>
      <p class="holder__role">Owner</p>
    </div>

    <ul class="contacts">
      <li class="contacts__item">
        <svg class="contacts__icon" viewBox="0 0 24 24" aria-hidden="true">
          <path fill="#ffffff" d="M6.6 10.8a15.1 15.1 0 0 0 6.6 6.6l2.2-2.2a1 1 0 0 1 1-.25 11.4 11.4 0 0 0 3.6.57 1 1 0 0 1 1 1V20a1 1 0 0 1-1 1A17 17 0 0 1 3 4a1 1 0 0 1 1-1h3.5a1 1 0 0 1 1 1c0 1.25.2 2.45.57 3.57a1 1 0 0 1-.25 1z"/>
        </svg>
        <span>555-418-2706</span>
      </li>
      <li class="contacts__item">
        <span class="contacts__dot" aria-hidden="true"></span>
        <span>everydrawerneatlysorted</span>
      </li>
      <li class="contacts__item">
        <svg class="contacts__icon" viewBox="0 0 24 24" aria-hidden="true">
          <path fill="none" stroke="#ffffff" stroke-width="2.2" stroke-linecap="round" d="M10 14a4 4 0 0 0 5.7 0l3-3a4 4 0 0 0-5.7-5.7l-1.2 1.2M14 10a4 4 0 0 0-5.7 0l-3 3a4 4 0 0 0 5.7 5.7l1.2-1.2"/>
        </svg>
        <span>www.ednorganized-example.com</span>
      </li>
    </ul>

    <p class="brand">Every Drawer<br>Neatly Sorted</p>
  </article>
</body>
</html>
```